Quarrow financial services, is a financial company that provides consultancy, brokerage services, and funding.

we will be providing the clients with insights, knowledge and data with regards to the financial markets.

with the brokerage services we will try to find the suitable counterparts that provide them with the best investments that suits their needs and expected return.

Target Market(s)

financial institutions, Corporates, high-net worth individuals

Industry/Entity Type

Financial Service

Contact Information for Business Card

Font styles to use
Other font styles liked:
• applemyungjo

Colors
00a990
848484

Requirements
Must have
• the logo at the back
Nice to have
• Finesse
Should not have
• boldness

```html
<!DOCTYPE html>
<html lang="en">
<head>
<meta charset="utf-8">
<title>Quarrow Financial Services – Business Card</title>
<link rel="stylesheet" href="https://fonts.googleapis.com/css2?family=Cinzel:wght@400&family=Tinos&family=Roboto:wght@400;500&display=swap">
<style>
  :root {
    --canvas: #e4e4e2;
    --card: #ffffff;
    --ink: #37403f;
    --muted: #555b5a;
    --teal: #2f8a78;
    --teal-accent: #00a990;
    --grey: #707070;
    --mark: #c9d5b6;
  }
  * { margin: 0; padding: 0; box-sizing: border-box; }
  html, body { width: 1200px; height: 443px; overflow: hidden; }
  body { background: var(--canvas); position: relative; }

  .card {
    position: absolute;
    top: 72px;
    height: 293px;
    background: var(--card);
    border-radius: 14px;
    overflow: hidden;
    box-shadow: 0 3px 6px rgba(0,0,0,.18);
  }
  .card--front { left: 82px; width: 484px; }
  .card--back  { left: 602px; width: 481px; }

  /* Front */
  .front-mark {
    position: absolute; left: 212px; top: 52px;
    width: 60px; height: 60px; background: var(--mark);
  }
  .front-name {
    position: absolute; left: 0; right: 0; top: 170px;
    text-align: center; font-family: "Cinzel", serif;
    color: var(--ink); font-size: 39px; letter-spacing: 2px; line-height: 1;
  }
  .front-sub {
    position: absolute; left: 0; right: 0; top: 208px;
    text-align: center; font-family: "Cinzel", serif;
    color: var(--ink); font-size: 13px; letter-spacing: 3.5px; line-height: 1.2;
  }
  .front-tagline {
    position: absolute; left: 0; right: 0; top: 229px;
    text-align: center; font-family: "Cinzel", serif;
    color: var(--ink); font-size: 9.5px; letter-spacing: .3px; line-height: 1.2;
  }

  /* Back */
  .back-waves { position: absolute; left: 0; top: 0; }
  .back-mark {
    position: absolute; left: 30px; top: 40px;
    width: 36px; height: 36px; background: var(--mark);
  }
  .back-name {
    position: absolute; left: 92px; top: 42px;
    font-family: "Cinzel", serif; color: var(--ink);
    font-size: 34px; letter-spacing: 1px; line-height: 1;
  }
  .back-sub {
    position: absolute; left: 92px; top: 74px; width: 188px;
    text-align: center; font-family: "Cinzel", serif; color: var(--ink);
    font-size: 10.5px; letter-spacing: 3px; line-height: 1.2;
  }
  .contact-list {
    position: absolute; left: 28px; top: 135px; list-style: none;
    font-family: "Tinos", serif; color: var(--muted); font-size: 14px;
  }
  .contact-list li { display: flex; align-items: center; height: 17.5px; }
  .contact-list svg { width: 11px; height: 11px; margin-right: 13px; fill: var(--teal); }
  .address {
    position: absolute; left: 28px; top: 192px;
    font-family: "Tinos", serif; color: var(--muted); font-size: 14px; line-height: 17.5px;
  }
  .person {
    position: absolute; right: 36px; top: 228px; text-align: right;
    font-family: "Roboto", sans-serif; color: #fff;
  }
  .person-name { font-size: 20px; font-weight: 500; letter-spacing: .3px; line-height: 1.1; }
  .person-role { font-size: 12px; margin-top: 7px; }
</style>
</head>
<body>
  <section class="card card--front">
    <div class="front-mark"></div>
    <div class="front-name">QUARROW</div>
    <div class="front-sub">FINANCIAL SERVICES</div>
    <div class="front-tagline">Clear insight for every financial decision</div>
  </section>

  <section class="card card--back">
    <svg class="back-waves" width="481" height="293" viewBox="0 0 481 293">
      <path d="M0,293 L0,272 C140,305 300,250 481,160 L481,293 Z" fill="var(--teal)"/>
      <path d="M0,230 C150,290 300,228 481,146 L481,157 C300,240 150,302 0,244 Z" fill="var(--grey)"/>
      <path d="M40,250 C170,282 300,246 390,212 C310,252 170,292 40,250 Z" fill="var(--grey)"/>
    </svg>

    <div class="back-mark"></div>
    <div class="back-name">QUARROW</div>
    <div class="back-sub">FINANCIAL SERVICES</div>

    <ul class="contact-list">
      <li><svg viewBox="0 0 12 12"><path d="M1 4c0-2 2-3 5-3s5 1 5 3l-2 1-1-2H4L3 5zM3 6h6l1 5H2z"/></svg>00-214-555-0193</li>
      <li><svg viewBox="0 0 12 12"><circle cx="6" cy="6" r="5.5"/><path d="M.5 6h11M6 .5c-3 3-3 8 0 11M6 .5c3 3 3 8 0 11" stroke="#fff" stroke-width=".8" fill="none"/></svg>www.quarrowfinance.com</li>
      <li><svg viewBox="0 0 12 12"><rect x="0.5" y="2" width="11" height="8"/><path d="M.5 2L6 7l5.5-5" stroke="#fff" stroke-width=".9" fill="none"/></svg>emarsh@quarrowfinance.com</li>
    </ul>
    <p class="address">1420 Alder Crest Lane<br>Fairmont California 90210</p>

    <div class="person">
      <div class="person-name">Elliot Marsh</div>
      <div class="person-role">Managing Director</div>
    </div>
  </section>
</body>
</html>
```